Animated (HTML5) banner ad for fantasy football (soccer) app

We want to promote our app where users can:
- Create your fantasy team
- Get points when your players score in real life
- Challenge your friends in private competitions
- Select players from many different leagues: Titan Series, Summit Circuit, Vértix, Kampfrunde, Coppa Brio, Trophée 7, Meridian Trophy, ++
Please have a look here for screenshots and color palette: https://www.plandeck.example/file/Xk93mQpL2vRtZaWbNcEdHf/Video?node-id=0%3A1
Sizes:
1:1 (Square) - 1200 x 1200 pixels.
1.91:1 (Landscape) – 1200 x 628 pixels.
4:5 (Portrait) – 1200 x 1500 pixels.
Prefer the file to be in Google Web Designer, but other might work too.

```html
<!DOCTYPE html>
<html lang="en">
<head>
<meta charset="utf-8">
<title>Goaldeck – Create your fantasy team</title>
<link rel="stylesheet" href="https://fonts.googleapis.com/css2?family=Poppins:wght@500;700;800&display=swap">
<style>
  :root {
    --teal-light: #0f6470;
    --teal-mid: #0b5560;
    --teal-dark: #073f47;
    --orange: #ff8c00;
    --ink-teal: #0d4a52;
    --white: #ffffff;
    --ink: #111111;
    --flag-white: #f4f4f4;
    --flag-blue: #1d8fe0;
    --flag-red: #e8261b;
  }
  html, body {
    margin: 0;
    padding: 0;
    overflow: hidden;
    background: var(--teal-dark);
  }
  .banner {
    position: relative;
    width: 1200px;
    height: 1195px;
    overflow: hidden;
    font-family: "Poppins", sans-serif;
    color: var(--white);
    background: radial-gradient(ellipse 70% 60% at 50% 45%, var(--teal-light) 0%, var(--teal-mid) 55%, var(--teal-dark) 100%);
  }
  .banner__flags {
    position: absolute;
    top: 0;
    left: 0;
    width: 1200px;
    height: 320px;
  }
  .brand {
    position: absolute;
    top: 112px;
    left: 0;
    width: 100%;
    text-align: center;
    font-weight: 800;
    font-size: 76px;
    line-height: 1;
    letter-spacing: 2px;
    color: var(--white);
  }
  .headline {
    position: absolute;
    top: 338px;
    left: 0;
    width: 100%;
    margin: 0;
    text-align: center;
    font-weight: 500;
    font-size: 72px;
    line-height: 1;
  }
  .headline__highlight {
    position: absolute;
    top: 439px;
    left: 108px;
    width: 988px;
    height: 141px;
    background: var(--orange);
    color: var(--ink-teal);
    font-weight: 800;
    font-size: 100px;
    line-height: 141px;
    text-align: center;
    letter-spacing: 2px;
  }
  .pitch {
    position: absolute;
    top: 638px;
    left: 0;
    width: 100%;
    margin: 0;
    text-align: center;
    font-weight: 700;
    font-size: 80px;
    line-height: 88px;
  }
  .pitch__accent {
    color: var(--orange);
  }
  .cta {
    position: absolute;
    top: 980px;
    left: 350px;
    width: 502px;
    height: 123px;
    border-radius: 36px;
    background: var(--orange);
    color: var(--ink);
    font-weight: 700;
    font-size: 44px;
    line-height: 123px;
    text-align: center;
    text-decoration: none;
  }
</style>
</head>
<body>
  <main class="banner">
    <svg class="banner__flags" viewBox="0 0 1200 320" aria-hidden="false">
      <defs>
        <radialGradient id="ball-tone" cx="40%" cy="35%" r="70%">
          <stop offset="0%" stop-color="#ffffff"/>
          <stop offset="70%" stop-color="#d9dcdf"/>
          <stop offset="100%" stop-color="#8d9399"/>
        </radialGradient>
      </defs>
      <g class="ribbon ribbon--left">
        <polygon points="0,72 200,96 200,140 0,136" fill="var(--flag-white)"/>
        <polygon points="0,136 200,140 200,190 0,200" fill="var(--flag-blue)"/>
        <polygon points="0,200 200,190 200,238 0,262" fill="var(--flag-red)"/>
      </g>
      <g class="ribbon ribbon--right">
        <polygon points="1200,72 1000,96 1000,140 1200,136" fill="var(--flag-white)"/>
        <polygon points="1200,136 1000,140 1000,190 1200,200" fill="var(--flag-blue)"/>
        <polygon points="1200,200 1000,190 1000,238 1200,262" fill="var(--flag-red)"/>
      </g>
      <circle cx="267" cy="159" r="100" fill="url(#ball-tone)" role="img" aria-label="Soccer ball illustration"/>
      <circle cx="933" cy="159" r="100" fill="url(#ball-tone)" role="img" aria-label="Soccer ball illustration"/>
    </svg>

    <div class="brand">GOALDECK</div>

    <h1 class="headline">Create your</h1>
    <div class="headline__highlight">FANTASY TEAM</div>

    <p class="pitch">Get points when<br>your players<br><span class="pitch__accent">score</span> in real life</p>

    <a class="cta" href="#register">REGISTER NOW</a>
  </main>
</body>
</html>
```